Worldwide Forum on Tension Molecules

We are arranging a meeting in Finland in August: THE 8th WORLDWIDE FORUM ON TENSION MOLECULES IN LIFE AND HEALING - TENSION HANDLING ROUTES AND CIRCUITS.

The program and speakers are included in the Word files. The basic poster arrangement could be a little bit like in the Conference:
http://events.qarvu.net/files/posters/1483956274_17-modulators-ferns.pdf

Basically only the organizers and invited speakers will be listed.

We would like to have some summery maritime background of the kind provided in the stock footage. In addition, we would include some summer views from the City of Turku. We have added a few potential University Campus views in the footage folder.
Updates

Project Deadline Extended
Reason: There was one design that was attractive. We wanted to extend the time available to work along the approach of this design.

Target Market(s)

Scientists in the field of cell stress research

Industry/Entity Type

Management

Requirements
Must have
• There must be the logo of our home university:
• https://www.veltrin.fi/personal/media/3991/vtenglogobasic4c.jpg
• ...somewhere down on the poster, a little bit like QARV in the example above.
• There must also be the logo of the organizing organization Tissue Strain Global Union:
• http://www.tissuestrainreplies.org/?
• All text should be readable (no light text on light background and vice versa)

```html
<!DOCTYPE html>
<html lang="en">
<head>
<meta charset="utf-8">
<title>Worldwide Forum on Tension Molecules – Poster</title>
<link rel="stylesheet" href="https://fonts.googleapis.com/css2?family=Signika:wght@400;600;700&family=Source+Sans+3:ital,wght@0,400;0,600;1,400;1,600;1,700&family=Playfair+Display:ital,wght@1,700&display=swap">
<style>
  :root {
    --page-bg: #e9e9e7;
    --sky-top: #6aa0ea;
    --sky-mid: #8fbaf0;
    --sky-low: #a9c8ef;
    --park-tree: #5d7a44;
    --park-lawn: #4f8a2e;
    --park-dark: #2f3b2a;
    --title-grey: #505357;
    --title-light: #f3f4f6;
    --ink: #1f2226;
    --panel-blue: rgba(104, 118, 140, 0.78);
    --panel-band: #434b57;
    --panel-light: rgba(236, 240, 246, 0.86);
    --panel-green: #3e8e5a;
    --accent-red: #e3202a;
    --accent-yellow: #ffe23a;
    --badge-brown: #8a3b1d;
    --union-green: #2c9c74;
    --white: #ffffff;
  }
  * { box-sizing: border-box; margin: 0; padding: 0; }
  html, body { width: 1200px; height: 900px; overflow: hidden; background: var(--page-bg); }
  body { position: relative; font-family: "Source Sans 3", sans-serif; }

  .poster {
    position: absolute; left: 296px; top: 21px;
    width: 607px; height: 857px; overflow: hidden;
    box-shadow: 0 4px 14px rgba(0,0,0,0.25);
  }
  .sky-photo {
    position: absolute; inset: 0 0 330px 0;
    background: linear-gradient(180deg, var(--sky-top) 0%, var(--sky-mid) 60%, var(--sky-low) 100%);
  }
  .park-photo {
    position: absolute; left: 0; right: 0; bottom: 0; height: 360px;
    background: linear-gradient(180deg, var(--sky-low) 0%, #b9c6b4 20%, var(--park-tree) 45%, var(--park-lawn) 72%, var(--park-dark) 100%);
  }

  .host-name {
    position: absolute; left: 34px; top: 56px;
    display: flex; align-items: center; gap: 10px;
    font-family: "Source Sans 3", sans-serif; font-weight: 600;
    font-size: 19px; line-height: 1.1; color: var(--ink);
  }
  .host-name .mark { width: 16px; height: 16px; background: var(--accent-red); }

  .edition-badge {
    position: absolute; left: 389px; top: 15px; width: 96px; height: 96px;
    border-radius: 50%; background: var(--white);
    border: 4px solid var(--badge-brown);
    box-shadow: inset 0 0 0 3px var(--white), inset 0 0 0 5px var(--badge-brown);
    display: flex; align-items: center; justify-content: center;
    font-family: "Playfair Display", serif; font-style: italic; font-weight: 700;
    color: var(--badge-brown); font-size: 50px; line-height: 1;
  }
  .edition-badge sup { font-size: 26px; vertical-align: 6px; }

  .forum-title {
    position: absolute; right: 22px; top: 124px; text-align: right;
    font-family: "Signika", sans-serif; font-weight: 600;
    font-size: 22.5px; line-height: 28px; color: var(--title-grey);
    text-transform: uppercase; letter-spacing: -0.2px;
  }
  .forum-theme {
    position: absolute; right: 20px; top: 218px; text-align: right;
    font-family: "Signika", sans-serif; font-weight: 700;
    font-size: 27px; line-height: 40px; color: var(--title-light);
    text-transform: uppercase; letter-spacing: -0.6px;
    text-shadow: 1px 1px 0 var(--title-grey), -1px -1px 0 var(--title-grey), 1px -1px 0 var(--title-grey), -1px 1px 0 var(--title-grey), 2px 3px 3px rgba(0,0,0,0.35);
  }
  .event-details {
    position: absolute; right: 24px; top: 302px; text-align: right;
    font-size: 16.5px; line-height: 21px; color: var(--ink);
  }
  .event-details .venue { font-style: italic; }

  .speakers-panel {
    position: absolute; left: 24px; top: 307px; width: 211px; height: 432px;
    background: var(--panel-blue); color: var(--white);
    font-size: 10.5px; line-height: 12.35px; font-weight: 600;
  }
  .speakers-panel .band { height: 6px; background: var(--panel-band); }
  .speakers-panel h2 {
    font-family: "Signika", sans-serif; font-weight: 600; font-size: 14px;
    text-align: center; margin: 3px 0 6px; color: var(--white);
  }
  .speakers-panel h2 .tag { color: var(--accent-yellow); }
  .speakers-panel .group { font-style: italic; font-weight: 400; padding-left: 6px; margin-bottom: 3px; }
  .speakers-panel .group em { color: var(--accent-red); }
  .speakers-panel ol { list-style: none; padding-left: 21px; margin-bottom: 5px; }
  .speakers-panel li .country { color: var(--accent-yellow); }
  .speakers-panel li.gap { height: 11px; }

  .organizers-panel {
    position: absolute; left: 363px; top: 384px; width: 222px; height: 324px;
    background: var(--panel-light); color: var(--ink);
    font-size: 13px; line-height: 15.5px; font-weight: 600;
  }
  .organizers-panel .band { height: 7px; background: var(--panel-green); }
  .organizers-panel h3 {
    font-style: italic; font-weight: 700; font-size: 16px;
    color: var(--accent-red); margin: 11px 0 6px 10px;
  }
  .organizers-panel .person { padding-left: 22px; margin-bottom: 8px; }

  .union-name {
    position: absolute; left: 22px; top: 815px;
    display: flex; align-items: center; gap: 8px;
    font-family: "Source Sans 3", sans-serif; font-weight: 600;
    font-size: 15px; color: var(--union-green);
  }
  .union-name .mark { width: 30px; height: 30px; border-radius: 50%; background: var(--white); }
</style>
</head>
<body>
  <main class="poster">
    <div class="sky-photo" role="img" aria-label="Summer sky with white clouds"></div>
    <div class="park-photo" role="img" aria-label="Summer park in Turku with a statue on a pedestal, tulip beds and old buildings"></div>

    <div class="host-name"><span class="mark"></span><span>Veltrin<br>University</span></div>

    <div class="edition-badge">8<sup>th</sup></div>

    <h1 class="forum-title">Worldwide Forum on<br>Tension Molecules in Life<br>and Healing</h1>
    <p class="forum-theme">Tension Handling Routes<br>and Circuits</p>

    <div class="event-details">
      <p>August 13-17, 2017</p>
      <p class="venue">Harborline Quay Hotel</p>
      <p>Turku, Finland</p>
    </div>

    <section class="speakers-panel">
      <div class="band"></div>
      <h2><span class="tag">TSGU Forum</span> 2017</h2>
      <p class="group"><em>Keynotes</em> (35 min + 10 min):</p>
      <ol>
        <li>1. Clara Windmere, <span class="country">UK</span></li>
        <li>2. Sanna Lehtovaara, <span class="country">Denmark</span></li>
        <li>3. Daniel Okabe, <span class="country">USA</span></li>
        <li>4. Martin Holloway, <span class="country">USA</span></li>
      </ol>
      <p class="group"><em>Invited speakers</em> (20 min + 10 min):</p>
      <ol>
        <li>1. Lucia Fernandes, <span class="country">Brazil</span></li>
        <li>2. Mirela Strand, <span class="country">USA</span></li>
        <li>3. Graham Pellow, <span class="country">USA</span></li>
        <li class="gap"></li>
        <li>5. Avner Levin, <span class="country">Israel</span></li>
        <li>6. Paolo Ricci, <span class="country">USA</span></li>
        <li>7. Elena Petrova-Marin, <span class="country">UK</span></li>
        <li>8. Steven R. Ashby, <span class="country">USA</span></li>
        <li>9. Inès Dumont, <span class="country">France</span></li>
        <li>10. Karen Whitfield, <span class="country">USA</span></li>
        <li>11. Joost Verhagen, <span class="country">The Netherlands</span></li>
        <li>12. Riikka Salmela, <span class="country">Finland</span></li>
        <li>13. Stefan K. Brandt, <span class="country">Germany</span></li>
        <li>14. Hélène Marchal, <span class="country">France</span></li>
        <li>15. Peter J. Lindqvist, <span class="country">USA</span></li>
        <li>16. Hiroshi Tanabe, <span class="country">Japan</span></li>
        <li>17. Kenji Moriya, <span class="country">Japan</span></li>
        <li>18. Paul Fenwick, <span class="country">USA</span></li>
        <li>19. R. Samir Haddad, <span class="country">USA</span></li>
        <li>20. Pekka T. Rautio, <span class="country">Finland</span></li>
        <li>21. Laura Benning, <span class="country">USA</span></li>
        <li>22. Chiara Bellini, <span class="country">Italy</span></li>
        <li>23. Thomas Garber, <span class="country">USA</span></li>
        <li>24. Robert A. Kessel, <span class="country">USA</span></li>
        <li>25. Ruth Mallory, <span class="country">USA</span></li>
      </ol>
    </section>

    <section class="organizers-panel">
      <div class="band"></div>
      <h3>ORGANIZER:</h3>
      <p class="person">Maija Kallio<br>Veltrin University<br>Finland</p>
      <h3>CO-ORGANIZERS:</h3>
      <p class="person">Henrik Ström<br>Veltrin University<br>and Saaren University<br>Finland</p>
      <p class="person">Walter Brennick<br>Tissue Strain Global Union<br>(TSGU)<br>Northfield State University<br>USA</p>
      <p class="person">Hélène Marchal<br>Université de Valmont<br>France</p>
    </section>

    <div class="union-name"><span class="mark"></span><span>Tissue Strain Global Union</span></div>
  </main>
</body>
</html>
```